依頼詳細
プロが業務用の高圧洗浄機を使い、ご自宅の外構・駐車場(ガレージ)・ブロック塀・玄関タイル・を綺麗にされたい方を募集します。
泥、排気ガスの汚れ、コケ、ほこり等を綺麗に致します。
お見積りは無料
高圧洗浄専門店
割引制度有
平日割引あり(火曜日・水曜日は特別料金にて実施)(空き状況はお電話にてご確認下さい)
施工料金等、丁寧に分かりやすくご説明します。
作業時間平均:2時間~3時間
料金:33,000円~
作業時:水道をお借りします
まずは、お気軽にご相談下さい。
株式会社ミドリノハウジング
TEL:094ー318-5562
担当:坂巻(さかまき)・梅沢(うめざわ)
営業時間:9:00~19:00

記載項目
株式会社ミドリノハウジング
094-318-5562
料金:33,000円~(範囲によって異なります)
プロの高圧洗浄はミドリノハウジングにお任せください。
サイズ
A4
ページ数
片面
希望イメージ
シンプル 複雑
単色 カラフル
暗い 明るい
日常 高級
遊び心 厳粛
未来的 伝統的
女性的 男性的
希望する色
水色系、ターコイズブルーの使用をお願い致します。
納品ファイル
• 高解像度JPG (.jpg)
補足説明
会社ロゴを添付しておりますので、ロゴの使用をお願い致します。
■ 選んだ理由

見やすく、弊社希望のチラシに近いものでした。
頂きました案件全てのチラシ案を印刷し、三つ折りにしましたが、一番良かったです。
伝えたい内容も、しっかり入っており、戸建てとなると年配の方が多いと思われ、その点でも大事な部分は文字が大きく見やすさも良く選ばせて頂きました。

■ 提案者全員のお礼・コメント

初めての依頼となりましたが、多数の応募を頂きましてありがとうございました。
正直、こんなに多数の応募を頂けるとは思ってませんでしたので驚きました。
今後もチラシの案をご依頼する事もるかと思いますので、宜しくお願い致します。

```html
<!DOCTYPE html>
<html lang="ja">
<head>
<meta charset="utf-8">
<title>高圧洗浄チラシ｜ミドリノハウジング</title>
<link href="https://fonts.googleapis.com/css2?family=M+PLUS+Rounded+1c:wght@500;700;800;900&family=Noto+Sans+JP:wght@400;500;700;900&display=swap" rel="stylesheet">
<style>
:root{
  --sky:#bfe6f6;
  --sky-deep:#5cc3e8;
  --turq:#1aa7d9;
  --navy:#0d2f6e;
  --red:#e8372c;
  --white:#ffffff;
  --ink:#1f2a44;
  --footer:#0f3a82;
}
*{margin:0;padding:0;box-sizing:border-box}
html,body{width:846px;height:1200px;overflow:hidden;background:#fff}
body{font-family:"Noto Sans JP",sans-serif;color:var(--ink)}
.flyer{position:relative;width:846px;height:1200px;overflow:hidden;background:linear-gradient(180deg,var(--sky) 0%,#e7f6fc 38%,#ffffff 60%)}
.abs{position:absolute;white-space:nowrap}

.lead-bar{left:60px;top:18px;width:726px;height:50px;background:var(--white);border-radius:25px;display:flex;align-items:center;justify-content:center;font-family:"M PLUS Rounded 1c",sans-serif;font-weight:800;font-size:26px;color:var(--navy);box-shadow:0 3px 0 var(--sky-deep)}
.lead-bar em{font-style:normal;color:var(--turq);font-size:30px}

.pro-tag{left:22px;top:86px;width:150px;height:110px;background:var(--turq);border-radius:18px;color:var(--white);font-family:"M PLUS Rounded 1c",sans-serif;font-weight:900;text-align:center;line-height:1.1;padding-top:14px;font-size:36px}
.pro-tag small{display:block;font-size:28px}

.headline{left:186px;top:74px;font-family:"M PLUS Rounded 1c",sans-serif;font-weight:900;font-size:90px;line-height:1.2;color:var(--navy);letter-spacing:2px;text-shadow:3px 3px 0 #fff,-3px -3px 0 #fff,3px -3px 0 #fff,-3px 3px 0 #fff}
.headline .small{font-size:72px}

.entrust{left:196px;top:196px;font-family:"M PLUS Rounded 1c",sans-serif;font-weight:800;font-size:28px;line-height:1.2;color:var(--navy)}

.worker{left:30px;top:250px;width:160px;height:250px;border-radius:80px 80px 20px 20px;background:linear-gradient(180deg,#9fd3ee,#3f8fc8)}

.free-badge{left:204px;top:244px;width:88px;height:88px;border-radius:50%;background:var(--red);color:#fff;font-weight:900;font-size:18px;line-height:1.15;display:flex;align-items:center;justify-content:center;text-align:center;white-space:normal}

.plan-box{left:300px;top:248px;width:392px;height:76px;background:#fff;border:4px solid var(--turq);border-radius:10px;display:flex;align-items:center;justify-content:center;font-family:"M PLUS Rounded 1c",sans-serif;font-weight:900;font-size:40px;line-height:1;color:var(--navy)}
.plan-note{left:704px;top:254px;width:120px;font-size:12.5px;line-height:1.4;color:var(--ink);white-space:normal}

.special{left:204px;top:340px;font-family:"M PLUS Rounded 1c",sans-serif;font-weight:800;font-size:27px;line-height:1.2;color:var(--red)}

.price{left:204px;top:378px;display:flex;align-items:flex-end;color:var(--red);font-family:"M PLUS Rounded 1c",sans-serif;font-weight:900;line-height:1}
.price .label{font-size:36px;line-height:1;width:38px;white-space:normal;margin-right:12px;margin-bottom:8px}
.price .amount{font-size:100px;letter-spacing:-2px}
.price .unit{font-size:48px;margin-left:4px;margin-bottom:8px}
.price .tax{font-size:20px;display:inline-block;margin-right:4px}
.price-line{left:204px;top:494px;width:620px;height:3px;background:var(--red)}

.notes{left:204px;top:506px;width:620px;display:grid;grid-template-columns:1fr 1fr;gap:4px 18px;font-size:13.5px;line-height:1.45;list-style:none}
.notes li::before{content:"●";color:var(--turq);margin-right:4px;font-size:11px}

.work-label{left:26px;top:580px;background:var(--navy);color:#fff;font-weight:700;font-size:17px;padding:4px 14px;border-radius:4px}
.house{left:26px;top:616px;width:410px;height:250px;border-radius:10px;background:linear-gradient(180deg,#d9eef8,#a9c7d9 60%,#8b9aa6)}
.spot{background:#fff;border:3px solid var(--turq);color:var(--navy);font-weight:700;font-size:16px;padding:4px 10px;border-radius:18px}
.wall{left:452px;top:580px;width:372px;height:286px;border-radius:10px;background:linear-gradient(135deg,#c6cfd4,#7f8b91)}
.dirt{width:96px;height:96px;border-radius:50%;background:#fff;border:4px solid var(--turq);display:flex;align-items:center;justify-content:center;text-align:center;font-family:"M PLUS Rounded 1c",sans-serif;font-weight:800;font-size:18px;color:var(--navy);line-height:1.2}
.sweep{left:650px;top:594px;background:var(--turq);color:#fff;font-family:"M PLUS Rounded 1c",sans-serif;font-weight:900;font-size:26px;padding:4px 14px;border-radius:6px}

.closing{left:0;top:884px;width:846px;height:62px;display:flex;align-items:center;justify-content:center;gap:10px;font-family:"M PLUS Rounded 1c",sans-serif;font-weight:800;font-size:18px;color:var(--red);background:#fff}
.closing span{color:var(--navy)}

.footer{left:0;top:946px;width:846px;height:254px;background:var(--footer);color:#fff}
.brand{left:28px;top:34px;display:flex;align-items:center;gap:12px}
.brand .mark{width:60px;height:60px;background:#fff;border-radius:8px}
.brand .name{font-weight:900;font-size:34px;letter-spacing:1px;line-height:1.2}
.brand .name small{font-size:18px;display:block;font-weight:900}
.address{left:28px;top:114px;font-size:14px}
.tel{left:28px;top:140px;display:flex;align-items:center;gap:10px;background:#fff;color:var(--navy);border-radius:8px;padding:4px 18px;font-family:"M PLUS Rounded 1c",sans-serif;font-weight:900;font-size:52px;line-height:1.1}
.hours{left:28px;top:218px;font-size:14px}
.operator{left:632px;top:26px;width:190px;height:228px;border-radius:95px 95px 0 0;background:linear-gradient(180deg,#f5d8c6,#6a9cc9)}
</style>
</head>
<body>
<div class="flyer">
  <div class="abs lead-bar">汚れが気になる<em>“住まいの外構”</em>を一掃しませんか？</div>

  <div class="abs pro-tag"><small>プロの</small>業務用</div>
  <div class="abs headline">高圧洗浄<span class="small">は</span></div>
  <div class="abs entrust">ミドリノハウジングにお任せください!!</div>

  <div class="abs worker" role="img" aria-label="高圧洗浄機を持った作業員のイラスト"></div>

  <div class="abs free-badge">お見積<br>無料</div>
  <div class="abs plan-box">平日割りプランあり</div>
  <div class="abs plan-note">空き状況は電話にてご確認下さい</div>
  <div class="abs special">火曜日・水曜日は特別料金で実施中♪</div>

  <div class="abs price">
    <span class="label">料<br>金</span>
    <span class="amount">33,000</span>
    <span class="unit"><span class="tax">税込</span>円〜</span>
  </div>
  <div class="abs price-line"></div>
  <ul class="abs notes">
    <li>料金は、洗浄範囲によって異なります。</li>
    <li>施工時はご自宅の水道をお借りします。</li>
    <li>平均作業時間は、2時間〜3時間程度です。</li>
    <li>高圧洗浄専門店の割引制度有。</li>
  </ul>

  <div class="abs work-label">主な施工箇所</div>
  <div class="abs house" role="img" aria-label="ガレージと玄関、ブロック塀のある一戸建て住宅のイラスト"></div>
  <div class="abs spot" style="left:34px;top:826px">ガレージ土間</div>
  <div class="abs spot" style="left:162px;top:826px">玄関周りのタイル</div>
  <div class="abs spot" style="left:322px;top:826px">ブロック塀</div>

  <div class="abs wall" role="img" aria-label="高圧洗浄で汚れを落としているブロック塀の写真"></div>
  <div class="abs sweep">高圧で一掃</div>
  <div class="abs dirt" style="left:466px;top:630px">排気ガス<br>汚れ</div>
  <div class="abs dirt" style="left:566px;top:700px">コケ</div>
  <div class="abs dirt" style="left:628px;top:768px">ほこり</div>
  <div class="abs dirt" style="left:722px;top:736px">泥汚れ</div>

  <div class="abs closing">施工料金など、分かりやすく丁寧にご説明します！<span>まずはお気軽にご相談ください！</span></div>

  <div class="abs footer">
    <div class="abs brand">
      <div class="mark"></div>
      <div class="name"><small>株式会社</small>ミドリノハウジング</div>
    </div>
    <div class="abs address">〒810-0099 福岡市中央区みどり台2-8-15 グリーンコート301</div>
    <div class="abs tel">
      <svg width="42" height="42" viewBox="0 0 24 24" aria-hidden="true"><path fill="#0d2f6e" d="M6.6 10.8a15.1 15.1 0 0 0 6.6 6.6l2.2-2.2a1 1 0 0 1 1-.25 11.4 11.4 0 0 0 3.6.57 1 1 0 0 1 1 1V20a1 1 0 0 1-1 1A17 17 0 0 1 3 4a1 1 0 0 1 1-1h3.5a1 1 0 0 1 1 1c0 1.25.2 2.45.57 3.57a1 1 0 0 1-.25 1z"/></svg>
      094-318-5562
    </div>
    <div class="abs hours">【営業時間】9時〜19時まで　【担当】坂巻(さかまき)・梅沢(うめざわ)</div>
    <div class="abs operator" role="img" aria-label="ヘッドセットを付けた受付スタッフのイラスト"></div>
  </div>
</div>
</body>
</html>
```